Artwork for pharmaceutical cream against eczema

We are a Belgian company launching a steroid-free cream for itchy, red and eczematic skin. It will be a 50 ml tube in a cardboard box. We are looking for a reliable, pharmaceutical, yet no sterile clinical, feel. A product a pharmacist would recommend, but you would not find in a general drug store or perfume shop. The name of the product is "Vumero". Colors to be used are deep blue, orange, black and white. The main color should not be black or white. The prominent use of the capital "S", like in the Drenoxa example should be considered. A design with a curved element that goes with the S, like in the Vitamin C example has the preference.

Reason: Hi all, I will extend the deadline with 5 days, because we feel that there is still not a perfect fit. Thanks Koen

Target Market(s)

Pharmacy. Broad public. Young parents with growing children.

Industry/Entity Type

Pharmacy

Font styles to use
Sans Serif

Requirements
Must have
• Text elements:
• "Vumero® crème"
• "50 g"
• "Bevat 1% hatseflats"
• "Verzorging van jeukende, rode en geïrriteerde huid"
Nice to have
• Side text elements (in plain black):
• "Lot 17XX17"
• "EXP 04/2020"
• Dummy EAN-13 barcode
• "Durno bvba - Vumerostraat 15 - 1234 Antwerpen"
• "Bevat Lorem ipsum dolor sit amet, consectetur adipiscing elit, sed do eiusmod tempor incididunt ut labore et dolore magna aliqua"

```html
<!DOCTYPE html>
<html lang="nl">
<head>
<meta charset="utf-8">
<title>Vumero crème – tube artwork</title>
<link rel="stylesheet" href="https://fonts.googleapis.com/css2?family=Arimo:wght@400;700&family=Roboto+Condensed:wght@700&display=swap">
<style>
  :root {
    --deep-blue: #24008f;
    --orange-light: #ffd21a;
    --orange-mid: #f39a12;
    --orange-deep: #c9420c;
    --rust: #8a2108;
    --white: #ffffff;
    --ink: #333333;
  }
  html, body {
    margin: 0;
    padding: 0;
    overflow: hidden;
    background: var(--white);
  }
  .tube-label {
    position: relative;
    width: 1200px;
    height: 265px;
    overflow: hidden;
    background:
      radial-gradient(ellipse 420px 240px at 520px 70px, var(--orange-light) 0%, rgba(255,210,26,0) 70%),
      radial-gradient(ellipse 900px 420px at 560px 120px, var(--orange-mid) 0%, var(--orange-deep) 65%, var(--rust) 100%);
    font-family: "Arimo", Arial, sans-serif;
  }
  .swoosh {
    position: absolute;
    inset: 0;
    width: 1200px;
    height: 265px;
  }
  .swoosh .panel { fill: var(--white); }
  .swoosh .band { fill: var(--deep-blue); }
  .claim {
    position: absolute;
    left: 54px;
    top: 32px;
    margin: 0;
    font-size: 24px;
    font-weight: 400;
    color: var(--white);
    letter-spacing: 0.2px;
  }
  .product-name {
    position: absolute;
    left: 806px;
    top: 46px;
    margin: 0;
    color: var(--ink);
    white-space: nowrap;
  }
  .product-name .brand {
    font-size: 62px;
    font-weight: 700;
    letter-spacing: -1px;
    line-height: 1;
  }
  .product-name .reg {
    position: relative;
    top: -32px;
    font-size: 18px;
    font-weight: 400;
  }
  .product-name .form {
    margin-left: 2px;
    font-size: 26px;
    font-weight: 400;
  }
  .usage {
    position: absolute;
    left: 676px;
    top: 206px;
    margin: 0;
    font-family: "Roboto Condensed", "Arial Narrow", sans-serif;
    font-weight: 700;
    font-size: 19px;
    color: var(--white);
  }
  .content {
    position: absolute;
    left: 1128px;
    top: 206px;
    margin: 0;
    font-family: "Roboto Condensed", "Arial Narrow", sans-serif;
    font-weight: 700;
    font-size: 26px;
    color: var(--white);
  }
</style>
</head>
<body>
  <main class="tube-label">
    <svg class="swoosh" viewBox="0 0 1200 265" aria-hidden="true">
      <path class="panel" d="M600 0 C720 75 920 120 1200 122 L1200 0 Z"/>
      <path class="band" d="M600 0 C720 75 920 120 1200 122 L1200 172 C900 166 660 95 556 0 Z"/>
      <path class="band" d="M0 188 C160 140 360 130 566 265 L520 265 C340 162 160 172 0 214 Z"/>
    </svg>

    <p class="claim">Bevat 1% hatseflats</p>

    <h1 class="product-name">
      <span class="brand">Vumero</span><span class="reg">®</span><span class="form">crème</span>
    </h1>

    <p class="usage">Verzorging van jeukende, rode en geïrriteerde huid</p>
    <p class="content">50g</p>
  </main>
</body>
</html>
```